40th Anniversary Gift - Summer of love

I want to have someone create a poster that feels like a vintage rock poster or Fernhollow anniversary poster in honor of my parents 40th anniversary. I have some original artwork from their engagement announcement from 1972 that is like to somehow incorporate but otherwise the creative is wide open. I just want some funk and soul!

Requirements
Must have
• An element from the original announcement which I will upload. No problem if you tweak or change the art or just add a piece somehow but I just want them to recognize that we used it somehow!

My parents names: Marla & Garrick

```html
<!DOCTYPE html>
<html lang="en">
<head>
<meta charset="utf-8">
<title>40th Anniversary — Marla &amp; Garrick</title>
<link rel="stylesheet" href="https://fonts.googleapis.com/css2?family=Yellowtail&family=Courgette&family=Pinyon+Script&display=swap">
<style>
  :root {
    --paper: #cdbd9f;
    --paper-light: #e2d8c2;
    --paper-edge: #6f6450;
    --rust: #8b5a2b;
    --rust-dark: #6e4320;
    --ink-blue: #34478f;
  }
  * { margin: 0; padding: 0; box-sizing: border-box; }
  html, body { width: 961px; height: 1200px; overflow: hidden; background: var(--paper); }
  .poster {
    position: relative;
    width: 961px;
    height: 1200px;
    overflow: hidden;
    background: var(--paper);
  }
  .sunburst, .rules { position: absolute; inset: 0; width: 961px; height: 1200px; }
  .vignette {
    position: absolute; inset: 0;
    background: radial-gradient(ellipse at 55% 45%, rgba(0,0,0,0) 45%, rgba(60,48,30,.45) 100%);
  }
  .headline-year {
    position: absolute; left: 270px; top: -10px;
    font-family: "Yellowtail", cursive;
    font-size: 200px; line-height: 1;
    color: var(--rust);
    transform: rotate(-7deg);
    transform-origin: left top;
  }
  .headline-anniversary {
    position: absolute; left: 330px; top: 290px;
    font-family: "Yellowtail", cursive;
    font-size: 34px; color: var(--rust-dark);
    transform: rotate(33deg);
    transform-origin: left top;
    letter-spacing: 1px;
  }
  .headline-love {
    position: absolute; left: 590px; top: 230px;
    font-family: "Yellowtail", cursive;
    font-size: 170px; line-height: 1;
    color: var(--rust);
    transform: rotate(-72deg);
    transform-origin: center;
  }
  .couple-art {
    position: absolute; left: 10px; top: 330px;
    width: 480px; height: 500px;
    border-radius: 40% 40% 30% 30%;
    background: radial-gradient(ellipse at 50% 50%, rgba(52,71,143,.42) 0%, rgba(52,71,143,.18) 55%, rgba(52,71,143,0) 75%);
  }
  .verse { position: absolute; font-family: "Pinyon Script", cursive; color: var(--ink-blue); font-size: 32px; white-space: nowrap; transform: rotate(14deg); transform-origin: left center; }
  .names {
    position: absolute; left: 30px; top: 870px;
    font-family: "Courgette", cursive;
    color: var(--rust);
    font-size: 78px; line-height: 1.05;
    transform: rotate(3deg);
  }
  .names span { display: block; }
  .names .amp { padding-left: 90px; }
</style>
</head>
<body>
<main class="poster">
  <svg class="sunburst" viewBox="0 0 961 1200" aria-hidden="true">
    <path fill="var(--paper-light)" opacity=".7" d="
      M850,300 L2850,300 L2820,648 Z
      M850,300 L2730,984 L2582,1300 Z
      M850,300 L2382,1586 L2136,1832 Z
      M850,300 L1850,2032 L1534,2180 Z
      M850,300 L1198,2270 L850,2300 Z
      M850,300 L502,2270 L166,2180 Z
      M850,300 L-150,2032 L-436,1832 Z
      M850,300 L-682,1586 L-882,1300 Z
      M850,300 L-1030,984 L-1120,648 Z
      M850,300 L-1150,300 L-1120,-48 Z
      M850,300 L-1030,-384 L-882,-700 Z
      M850,300 L-682,-986 L-436,-1232 Z
      M850,300 L-150,-1432 L166,-1580 Z
      M850,300 L502,-1670 L850,-1700 Z
      M850,300 L1198,-1670 L1534,-1580 Z
      M850,300 L1850,-1432 L2136,-1232 Z
      M850,300 L2382,-986 L2582,-700 Z
      M850,300 L2730,-384 L2820,-48 Z"/>
  </svg>
  <div class="vignette"></div>

  <svg class="rules" viewBox="0 0 961 1200" aria-hidden="true">
    <line x1="0" y1="50" x2="640" y2="490" stroke="var(--rust)" stroke-width="9" opacity=".85"/>
    <line x1="720" y1="170" x2="286" y2="1200" stroke="var(--rust)" stroke-width="9" opacity=".85"/>
  </svg>

  <h1 class="headline">
    <span class="headline-year">40th</span>
    <span class="headline-anniversary">anniversary</span>
    <span class="headline-love">Love</span>
  </h1>

  <div class="couple-art" role="img" aria-label="Ink drawing of an embracing couple seen from behind, with the word Love in script, from the 1972 engagement announcement"></div>

  <p class="announcement">
    <span class="verse" style="left:635px; top:555px;">is . . .</span>
    <span class="verse" style="left:590px; top:615px;">Marla G. Halloway</span>
    <span class="verse" style="left:688px; top:735px;">and</span>
    <span class="verse" style="left:552px; top:795px;">Garrick S. Brightwater</span>
    <span class="verse" style="left:612px; top:890px;">Engaged</span>
    <span class="verse" style="left:545px; top:975px;">the eighth of December</span>
    <span class="verse" style="left:392px; top:1045px;">nineteen hundred and seventy-two</span>
  </p>

  <h2 class="names">
    <span>Marla</span>
    <span class="amp">&amp;</span>
    <span>Garrick</span>
  </h2>
</main>
</body>
</html>
```